Custom beer tap decals, Halvett Brewery, Tasmania, Australia.

UPDATE 22/6/2017

Based on designs received so far, Im after more of a bold/clean design. This must standout. See attached example.

Beer tap decals for 4 different products. Rustic/English feel, with some modern vibrancy, maintain original branding as much as possible.
The size bust be a 95mm circle. Please see attached artwork.
The same branding theme must carry across all four designs. While each can be different, the core branding remaining the same is important.
Happy for different fonts to be used, but they must be clearly readable. The font for the 'Halvett Brewery' component must remain the same.
The colours used in the flag banner part of the decal must remain the same as these reflect the colours on our bottle labels.

Highlighting the 'Made in Tasmania' component would be nice, although not entirely necessary.

Plus a 'Limited Release; design including white space where one off beers can be written in permanent marker, we brew quite a few small batch beers per year and it doesn’t make sense to have custom decals for each. Having a generic limited release decal that we can change ourselves would be a big help.

Target Market(s)

Graphic design, beer, brewery.

Industry/Entity Type

Brewery

Colors

Designer to choose colors to be used in the design.

Requirements
Must have
• 'Halvett Brewery' component of supplied decals must remain. Would be nice to incorporate some of the shield elements, but isn't vital.
Nice to have
• Rustic/earth themes, with a modern twist and vibrance.

```html
<!DOCTYPE html>
<html lang="en">
<head>
<meta charset="utf-8">
<title>Halvett Brewery – Tap Decals</title>
<link rel="stylesheet" href="https://fonts.googleapis.com/css2?family=Cinzel:wght@700&family=Tinos:wght@400;700&display=swap">
<style>
  :root {
    --canvas: #efe9df;
    --ink: #2a2622;
    --face: #ffffff;
    --ribbon-light: #fff7e6;
    --pale-ale: #f08a2a;
    --irish-red: #b02a3c;
    --english-bitter: #c9a24a;
    --irish-stout: #dfe39a;
    --limited: #4ba046;
  }
  * { margin: 0; padding: 0; box-sizing: border-box; }
  html, body { width: 1200px; height: 933px; overflow: hidden; }
  body { background: var(--canvas); position: relative; }
  .decal-range { position: absolute; inset: 0; }
  .decal { position: absolute; top: 170px; width: 192px; height: 192px; display: block; }
  .decal--pale-ale { left: 47px; }
  .decal--irish-red { left: 266px; }
  .decal--english-bitter { left: 486px; }
  .decal--irish-stout { left: 709px; }
  .decal--limited { left: 939px; }

  .ring { fill: var(--tone); }
  .keyline { fill: none; stroke: var(--ink); stroke-width: 1.6; }
  .face { fill: var(--face); }
  .banner-body { fill: var(--tone); stroke: var(--ink); stroke-width: 1.2; }
  .banner-tail { fill: var(--tail); stroke: var(--ink); stroke-width: 1.2; }
  .hops { fill: url(#hopTone); }
  .brand-name { font-family: "Cinzel", serif; font-weight: 700; font-size: 21px; fill: var(--ink); letter-spacing: 0.5px; }
  .brand-sub { font-family: "Tinos", serif; font-size: 7px; fill: var(--ink); letter-spacing: 1.2px; }
  .beer-name { font-family: "Cinzel", serif; font-weight: 700; font-size: 11px; fill: var(--label-ink); }
  .abv { font-family: "Tinos", serif; font-size: 7.5px; fill: var(--ink); }
  .origin { font-family: "Tinos", serif; font-weight: 700; font-size: 7.5px; fill: var(--ink); letter-spacing: 0.4px; }

  .decal--pale-ale { --tone: var(--pale-ale); --tail: #c46a18; --label-ink: var(--ribbon-light); }
  .decal--irish-red { --tone: var(--irish-red); --tail: #86202e; --label-ink: var(--ribbon-light); }
  .decal--english-bitter { --tone: var(--english-bitter); --tail: #a3823a; --label-ink: var(--ink); }
  .decal--irish-stout { --tone: var(--irish-stout); --tail: #b9bd76; --label-ink: var(--ink); }
  .decal--limited { --tone: var(--limited); --tail: #357c32; --label-ink: var(--ink); }
</style>
</head>
<body>
<svg width="0" height="0" style="position:absolute" aria-hidden="true">
  <defs>
    <radialGradient id="hopTone" cx="50%" cy="45%" r="60%">
      <stop offset="0%" stop-color="#a8cc3c"/>
      <stop offset="100%" stop-color="#3f7a24"/>
    </radialGradient>
  </defs>
</svg>

<main class="decal-range">
  <svg class="decal decal--pale-ale" viewBox="0 0 200 200">
    <circle class="ring" cx="100" cy="100" r="100"/>
    <circle class="face" cx="100" cy="100" r="89"/>
    <circle class="keyline" cx="100" cy="100" r="89"/>
    <text class="brand-name" x="100" y="58" text-anchor="middle">HALVETT</text>
    <text class="brand-sub" x="100" y="68" text-anchor="middle">BREWERY</text>
    <path class="banner-tail" d="M30 76 L56 79 L56 103 L34 100 L42 88 Z"/>
    <path class="banner-tail" d="M170 76 L144 79 L144 103 L166 100 L158 88 Z"/>
    <path class="banner-body" d="M52 77 Q100 69 148 77 L148 105 Q100 97 52 105 Z"/>
    <text class="beer-name" x="100" y="89" text-anchor="middle" font-size="13">PALE</text>
    <text class="beer-name" x="100" y="100" text-anchor="middle" font-size="9">ALE</text>
    <ellipse class="hops" cx="46" cy="116" rx="22" ry="20" role="img" aria-label="Hop cones and leaves illustration"/>
    <ellipse class="hops" cx="154" cy="116" rx="22" ry="20" role="img" aria-label="Hop cones and leaves illustration"/>
    <text class="abv" x="100" y="134" text-anchor="middle">5% ABV</text>
    <text class="origin" x="100" y="157" text-anchor="middle">PROUDLY</text>
    <text class="origin" x="100" y="167" text-anchor="middle">TASMANIAN MADE</text>
  </svg>

  <svg class="decal decal--irish-red" viewBox="0 0 200 200">
    <circle class="ring" cx="100" cy="100" r="100"/>
    <circle class="face" cx="100" cy="100" r="89"/>
    <circle class="keyline" cx="100" cy="100" r="89"/>
    <text class="brand-name" x="100" y="58" text-anchor="middle">HALVETT</text>
    <text class="brand-sub" x="100" y="68" text-anchor="middle">BREWERY</text>
    <path class="banner-tail" d="M30 76 L56 79 L56 103 L34 100 L42 88 Z"/>
    <path class="banner-tail" d="M170 76 L144 79 L144 103 L166 100 L158 88 Z"/>
    <path class="banner-body" d="M52 77 Q100 69 148 77 L148 105 Q100 97 52 105 Z"/>
    <text class="beer-name" x="100" y="89" text-anchor="middle">IRISH RED</text>
    <text class="beer-name" x="100" y="100" text-anchor="middle" font-size="9">ALE</text>
    <ellipse class="hops" cx="46" cy="116" rx="22" ry="20" role="img" aria-label="Hop cones and leaves illustration"/>
    <ellipse class="hops" cx="154" cy="116" rx="22" ry="20" role="img" aria-label="Hop cones and leaves illustration"/>
    <text class="abv" x="100" y="134" text-anchor="middle">5.1%</text>
    <text class="origin" x="100" y="157" text-anchor="middle">PROUDLY</text>
    <text class="origin" x="100" y="167" text-anchor="middle">TASMANIAN MADE</text>
  </svg>

  <svg class="decal decal--english-bitter" viewBox="0 0 200 200">
    <circle class="ring" cx="100" cy="100" r="100"/>
    <circle class="face" cx="100" cy="100" r="89"/>
    <circle class="keyline" cx="100" cy="100" r="89"/>
    <text class="brand-name" x="100" y="58" text-anchor="middle">HALVETT</text>
    <text class="brand-sub" x="100" y="68" text-anchor="middle">BREWERY</text>
    <path class="banner-tail" d="M30 76 L56 79 L56 103 L34 100 L42 88 Z"/>
    <path class="banner-tail" d="M170 76 L144 79 L144 103 L166 100 L158 88 Z"/>
    <path class="banner-body" d="M52 77 Q100 69 148 77 L148 105 Q100 97 52 105 Z"/>
    <text class="beer-name" x="100" y="89" text-anchor="middle">ENGLISH</text>
    <text class="beer-name" x="100" y="100" text-anchor="middle" font-size="9.5">BITTER</text>
    <ellipse class="hops" cx="46" cy="116" rx="22" ry="20" role="img" aria-label="Hop cones and leaves illustration"/>
    <ellipse class="hops" cx="154" cy="116" rx="22" ry="20" role="img" aria-label="Hop cones and leaves illustration"/>
    <text class="abv" x="100" y="134" text-anchor="middle">4.2%</text>
    <text class="origin" x="100" y="157" text-anchor="middle">PROUDLY</text>
    <text class="origin" x="100" y="167" text-anchor="middle">TASMANIAN MADE</text>
  </svg>

  <svg class="decal decal--irish-stout" viewBox="0 0 200 200">
    <circle class="ring" cx="100" cy="100" r="100"/>
    <circle class="face" cx="100" cy="100" r="89"/>
    <circle class="keyline" cx="100" cy="100" r="89"/>
    <text class="brand-name" x="100" y="58" text-anchor="middle">HALVETT</text>
    <text class="brand-sub" x="100" y="68" text-anchor="middle">BREWERY</text>
    <path class="banner-tail" d="M30 76 L56 79 L56 103 L34 100 L42 88 Z"/>
    <path class="banner-tail" d="M170 76 L144 79 L144 103 L166 100 L158 88 Z"/>
    <path class="banner-body" d="M52 77 Q100 69 148 77 L148 105 Q100 97 52 105 Z"/>
    <text class="beer-name" x="100" y="89" text-anchor="middle">IRISH</text>
    <text class="beer-name" x="100" y="100" text-anchor="middle" font-size="9.5">STOUT</text>
    <ellipse class="hops" cx="46" cy="116" rx="22" ry="20" role="img" aria-label="Hop cones and leaves illustration"/>
    <ellipse class="hops" cx="154" cy="116" rx="22" ry="20" role="img" aria-label="Hop cones and leaves illustration"/>
    <text class="abv" x="100" y="134" text-anchor="middle">4.7%</text>
    <text class="origin" x="100" y="157" text-anchor="middle">PROUDLY</text>
    <text class="origin" x="100" y="167" text-anchor="middle">TASMANIAN MADE</text>
  </svg>

  <svg class="decal decal--limited" viewBox="0 0 200 200">
    <circle class="ring" cx="100" cy="100" r="100"/>
    <circle class="face" cx="100" cy="100" r="89"/>
    <circle class="keyline" cx="100" cy="100" r="89"/>
    <text class="brand-name" x="100" y="58" text-anchor="middle">HALVETT</text>
    <text class="brand-sub" x="100" y="68" text-anchor="middle">BREWERY</text>
    <path class="banner-tail" d="M30 76 L56 79 L56 103 L34 100 L42 88 Z"/>
    <path class="banner-tail" d="M170 76 L144 79 L144 103 L166 100 L158 88 Z"/>
    <path class="banner-body" d="M52 77 Q100 69 148 77 L148 105 Q100 97 52 105 Z"/>
    <ellipse class="hops" cx="46" cy="116" rx="22" ry="20" role="img" aria-label="Hop cones and leaves illustration"/>
    <ellipse class="hops" cx="154" cy="116" rx="22" ry="20" role="img" aria-label="Hop cones and leaves illustration"/>
    <text class="origin" x="100" y="157" text-anchor="middle">PROUDLY</text>
    <text class="origin" x="100" y="167" text-anchor="middle">TASMANIAN MADE</text>
  </svg>
</main>
</body>
</html>
```